PowerPoint Template Design for business consulting company in Silicon Valley

I need a PowerPoint template to use as the starting point for new presentations. I have a logo but now need design that supports this. I've attached a very descriptive PDF that explains exactly what I need. Here is a list of deliverables: 1. PowerPoint Template that I will use as the starter presentation for all new Vantor Bellway presentationsDesigns for the following slides: See picture below for examples of structure:2. Title slide with subtitle3. Section header4. Title and body5. Title and 2 columns6. Title and 3 columns7. One column text8. Editable timeline to show months, or steps for a process9. Bullet design for unordered list (can be graphic)10. Bullet design for ordered list11. Recommended fonts for each design: Title, subtitle, list, captionOPTIONAL: Possible graphic elements to be used for section title slide backgrounds or graphic elements:--Your team / my team / people on project--Goals for project / presentation--Editable Timeline--Speaking--Writing--Listening--People collaborating / helping each otherI am happy to accept proposals for developing these optional elements in a separate project.

Requirements
Must have
• Must be FLAT design.
• Not flashy or garish. Must be subtle.

```html
<!DOCTYPE html>
<html lang="en">
<head>
<meta charset="utf-8">
<title>Vantor Bellway – Presentation Template</title>
<link rel="stylesheet" href="https://fonts.googleapis.com/css2?family=Marcellus&family=Crimson+Text:wght@400;600&display=swap">
<style>
  :root {
    --blue: #1f3b94;
    --green: #1b6d2f;
    --white: #ffffff;
    --rule-grey: #e4e4e4;
    --text-grey: #555555;
    --text-dark: #2a2a2a;
    --stage-light: #ececec;
    --stage-dark: #5a5a5a;
    --title-font: "Marcellus", "Times New Roman", serif;
    --body-font: "Crimson Text", Georgia, serif;
  }
  * { box-sizing: border-box; margin: 0; padding: 0; }
  html, body { width: 734px; height: 1200px; overflow: hidden; }
  body { position: relative; background: var(--stage-dark); font-family: var(--body-font); }

  .stage-top { position: absolute; left: 0; top: 0; width: 734px; height: 482px; background: var(--stage-light); }
  .stage-grid { position: absolute; left: 0; top: 482px; width: 734px; height: 718px; background: var(--stage-dark); }

  .slide {
    position: absolute; width: 334px; height: 188px; background: var(--white);
    overflow: hidden; box-shadow: 0 6px 14px rgba(0,0,0,0.28);
  }
  .slide--hero { left: 47px; top: 62px; transform: scale(1.916); transform-origin: 0 0; box-shadow: 0 3px 8px rgba(0,0,0,0.18); }

  .pos-1 { left: 16px; top: 22px; }
  .pos-2 { left: 384px; top: 22px; }
  .pos-3 { left: 16px; top: 258px; }
  .pos-4 { left: 384px; top: 258px; }
  .pos-5 { left: 16px; top: 494px; }
  .pos-6 { left: 384px; top: 494px; }

  /* title slide */
  .cover-panel { position: absolute; left: 0; top: 0; width: 334px; height: 188px; }
  .cover-lines { position: absolute; left: 3px; top: 0; width: 3px; height: 188px; border-left: 0.6px solid rgba(255,255,255,0.6); border-right: 0.6px solid rgba(255,255,255,0.6); }
  .cover-rule { position: absolute; left: 17px; top: 34px; width: 14px; height: 1.2px; background: var(--white); }
  .cover-title { position: absolute; left: 17px; top: 40px; font-family: var(--title-font); font-weight: 400; font-size: 14px; line-height: 20.5px; color: var(--white); text-transform: uppercase; letter-spacing: 0.2px; }
  .cover-sub { position: absolute; left: 17px; top: 134px; width: 125px; font-size: 4.6px; line-height: 6px; color: var(--white); }
  .cover-brand { position: absolute; left: 180px; top: 66px; width: 140px; text-align: center; font-family: var(--title-font); font-size: 21px; line-height: 25px; color: var(--blue); }

  /* content slide chrome */
  .slide-bar { position: absolute; left: 0; top: 0; width: 334px; height: 24px; }
  .slide-title { position: absolute; left: 0; top: 0; width: 244px; height: 24px; padding-left: 6px; background: var(--green); color: var(--white); font-family: var(--title-font); font-weight: 400; font-size: 11.5px; line-height: 24px; }
  .brand-mark { position: absolute; left: 252px; top: 3px; width: 66px; text-align: center; font-family: var(--title-font); font-size: 7.5px; line-height: 8px; color: var(--blue); }
  .brand-tab { position: absolute; right: 0; top: 0; width: 12px; height: 24px; background: var(--blue); }
  .slide-foot { position: absolute; left: 0; bottom: 5px; width: 334px; height: 5px; background: var(--rule-grey); }
  .web-address { position: absolute; left: 0; top: 0; width: 334px; text-align: center; font-size: 3.4px; line-height: 5px; letter-spacing: 0.8px; color: var(--text-grey); }
  .page-number { position: absolute; right: 6px; top: -2.5px; width: 9px; height: 9px; border-radius: 50%; background: var(--green); color: var(--white); font-size: 5px; line-height: 9px; text-align: center; }

  .photo { position: absolute; }
  .photo--meeting-hands { left: 0; top: 44px; width: 145px; height: 124px; background: linear-gradient(135deg, #d9dde2 0%, #b9c0c8 45%, #e8e5e0 100%); }
  .photo--team { left: 144px; top: 28px; width: 190px; height: 148px; background: linear-gradient(160deg, #f4f4f4 0%, #d7d2cc 45%, #5a4a40 80%, #3a3330 100%); }

  .toc { position: absolute; left: 157px; top: 49px; width: 156px; list-style: none; }
  .toc li { display: flex; align-items: center; height: 17.4px; font-size: 5px; color: var(--text-dark); }
  .toc .toc-leader { flex: 1; margin: 0 4px; border-bottom: 0.6px dashed #888; }

  .body-copy { position: absolute; left: 7px; top: 48px; width: 126px; font-size: 4.9px; line-height: 9.4px; color: var(--text-dark); }

  /* section header */
  .section-bg { position: absolute; inset: 0; background: linear-gradient(180deg, #4d9a3f 0%, #3d8a3a 55%, #2f7a34 100%); }
  .section-frame { position: absolute; left: 5px; top: 5px; width: 324px; height: 178px; border: 0.8px solid rgba(255,255,255,0.85); }
  .section-title { position: absolute; left: 52px; top: 75px; width: 228px; height: 37px; border: 1px solid var(--white); color: var(--white); font-family: var(--title-font); font-weight: 400; font-size: 22px; line-height: 35px; text-align: center; }

  /* column cards */
  .col-card { position: absolute; top: 67px; height: 89px; background: var(--blue); color: var(--white); text-align: center; padding: 21px 6px 0; }
  .col-card::before { content: ""; position: absolute; left: 50%; top: 0; transform: translateX(-50%); border-left: 7px solid transparent; border-right: 7px solid transparent; border-top: 7px solid var(--white); }
  .col-card h3 { font-family: var(--body-font); font-weight: 400; font-size: 7.5px; line-height: 9px; text-decoration: underline; margin-bottom: 5px; }
  .col-card p { font-size: 5px; line-height: 9.4px; }
  .col-card--wide { width: 109px; }
  .col-card--narrow { width: 92px; }
  .col-icon { position: absolute; top: 48px; width: 17px; height: 17px; }
</style>
</head>
<body>

<div class="stage-top">
  <section class="slide slide--hero">
    <svg class="cover-panel" viewBox="0 0 334 188" aria-hidden="true">
      <path d="M0 0 H172 Q118 94 178 188 H0 Z" fill="var(--blue)"/>
    </svg>
    <span class="cover-lines"></span>
    <span class="cover-rule"></span>
    <h1 class="cover-title">The<br>Presentation<br>Title Goes<br>Here</h1>
    <p class="cover-sub">Lorem Ipsum is simply dummy text of the printing and typesetting industry. Lorem Ipsum has been the industry's standard dummy text.</p>
    <div class="cover-brand">Vantor<br>Bellway</div>
  </section>
</div>

<div class="stage-grid">

  <!-- title slide -->
  <section class="slide pos-1">
    <svg class="cover-panel" viewBox="0 0 334 188" aria-hidden="true">
      <path d="M0 0 H172 Q118 94 178 188 H0 Z" fill="var(--blue)"/>
    </svg>
    <span class="cover-lines"></span>
    <span class="cover-rule"></span>
    <h1 class="cover-title">The<br>Presentation<br>Title Goes<br>Here</h1>
    <p class="cover-sub">Lorem Ipsum is simply dummy text of the printing and typesetting industry. Lorem Ipsum has been the industry's standard dummy text.</p>
    <div class="cover-brand">Vantor<br>Bellway</div>
  </section>

  <!-- contents slide -->
  <section class="slide pos-2">
    <header class="slide-bar">
      <h2 class="slide-title">Title Goes Here</h2>
      <div class="brand-mark">Vantor<br>Bellway</div>
      <span class="brand-tab"></span>
    </header>
    <div class="photo photo--meeting-hands" role="img" aria-label="Photo of hands with a pen reviewing a document at a desk"></div>
    <ol class="toc">
      <li>Title Goes Here<span class="toc-leader"></span>03</li>
      <li>Title Goes Here<span class="toc-leader"></span>04</li>
      <li>Title Goes Here<span class="toc-leader"></span>05</li>
      <li>Title Goes Here<span class="toc-leader"></span>06</li>
      <li>Title Goes Here<span class="toc-leader"></span>07</li>
      <li>Title Goes Here<span class="toc-leader"></span>08</li>
      <li>Title Goes Here<span class="toc-leader"></span>09</li>
    </ol>
    <footer class="slide-foot"><span class="web-address">www.webaddress.com</span><span class="page-number">2</span></footer>
  </section>

  <!-- section header -->
  <section class="slide pos-3">
    <div class="section-bg" role="img" aria-label="Soft green photo of an alarm clock, young plants and stacked coins"></div>
    <span class="section-frame"></span>
    <h2 class="section-title">SECTION HEADER</h2>
  </section>

  <!-- title and body -->
  <section class="slide pos-4">
    <header class="slide-bar">
      <h2 class="slide-title">Title Goes Here</h2>
      <div class="brand-mark">Vantor<br>Bellway</div>
      <span class="brand-tab"></span>
    </header>
    <p class="body-copy">Lorem Ipsum is simply dummy text of the printing and typesetting industry. Lorem Ipsum has been the industry's standard dummy text ever since the 1500s, when an unknown printer took a galley of type and scrambled it to make a type specimen book. It has survived not only five centuries, but also the leap into electronic typesetting, remaining essentially unchanged. It was popularised in the 1960s with the release of Pressline sheets containing Lorem Ipsum passages, and more recently with desktop publishing software like Folio Layout including versions of Lorem Ipsum.</p>
    <div class="photo photo--team" role="img" aria-label="Photo of a business team shaking hands around a meeting table"></div>
    <footer class="slide-foot"><span class="web-address">www.webaddress.com</span><span class="page-number">4</span></footer>
  </section>

  <!-- two columns -->
  <section class="slide pos-5">
    <header class="slide-bar">
      <h2 class="slide-title">Title Goes Here</h2>
      <div class="brand-mark">Vantor<br>Bellway</div>
      <span class="brand-tab"></span>
    </header>
    <svg class="col-icon" style="left:84px" viewBox="0 0 16 16" aria-hidden="true">
      <circle cx="8" cy="3" r="2.4" fill="#1a1a1a"/>
      <circle cx="4" cy="8" r="1.8" fill="#1a1a1a"/><circle cx="12" cy="8" r="1.8" fill="#1a1a1a"/>
      <path d="M1 16 V12.5 Q1 10.2 4 10.2 Q7 10.2 7 12.5 V16 Z M9 16 V12.5 Q9 10.2 12 10.2 Q15 10.2 15 12.5 V16 Z" fill="#1a1a1a"/>
    </svg>
    <div class="col-card col-card--wide" style="left:38px">
      <h3>1st Column</h3>
      <p>Lorem Ipsum is simply dummy text of the printing and typesetting industry. Lorem Ipsum has been the industry's standard dummy text ever since the 1500s.</p>
    </div>
    <svg class="col-icon" style="left:233px" viewBox="0 0 16 16" aria-hidden="true">
      <circle cx="4" cy="3.5" r="2" fill="#1a1a1a"/><circle cx="12" cy="3.5" r="2" fill="#1a1a1a"/>
      <path d="M1 16 V9 Q1 6.5 4 6.5 Q7 6.5 7 9 V16 Z M9 16 V9 Q9 6.5 12 6.5 Q15 6.5 15 9 V16 Z" fill="#1a1a1a"/>
    </svg>
    <div class="col-card col-card--wide" style="left:187px">
      <h3>2nd Column</h3>
      <p>Lorem Ipsum is simply dummy text of the printing and typesetting industry. Lorem Ipsum has been the industry's standard dummy text ever since the 1500s.</p>
    </div>
    <footer class="slide-foot"><span class="web-address">www.webaddress.com</span><span class="page-number">5</span></footer>
  </section>

  <!-- three columns -->
  <section class="slide pos-6">
    <header class="slide-bar">
      <h2 class="slide-title">Title Goes Here</h2>
      <div class="brand-mark">Vantor<br>Bellway</div>
      <span class="brand-tab"></span>
    </header>
    <svg class="col-icon" style="left:42.5px" viewBox="0 0 16 16" aria-hidden="true">
      <circle cx="8" cy="3" r="2.4" fill="#1a1a1a"/>
      <circle cx="4" cy="8" r="1.8" fill="#1a1a1a"/><circle cx="12" cy="8" r="1.8" fill="#1a1a1a"/>
      <path d="M1 16 V12.5 Q1 10.2 4 10.2 Q7 10.2 7 12.5 V16 Z M9 16 V12.5 Q9 10.2 12 10.2 Q15 10.2 15 12.5 V16 Z" fill="#1a1a1a"/>
    </svg>
    <div class="col-card col-card--narrow" style="left:5px">
      <h3>1st Column</h3>
      <p>Lorem Ipsum is simply dummy text of the printing and typesetting industry. Lorem Ipsum has been the industry's standard dummy text ever.</p>
    </div>
    <svg class="col-icon" style="left:158.5px" viewBox="0 0 16 16" aria-hidden="true">
      <circle cx="4" cy="3.5" r="2" fill="#1a1a1a"/><circle cx="12" cy="3.5" r="2" fill="#1a1a1a"/>
      <path d="M1 16 V9 Q1 6.5 4 6.5 Q7 6.5 7 9 V16 Z M9 16 V9 Q9 6.5 12 6.5 Q15 6.5 15 9 V16 Z" fill="#1a1a1a"/>
    </svg>
    <div class="col-card col-card--narrow" style="left:121px">
      <h3>2nd Column</h3>
      <p>Lorem Ipsum is simply dummy text of the printing and typesetting industry. Lorem Ipsum has been the industry's standard dummy text ever.</p>
    </div>
    <svg class="col-icon" style="left:273.5px" viewBox="0 0 16 16" aria-hidden="true">
      <rect x="1" y="1" width="8" height="15" fill="#1a1a1a"/>
      <rect x="2.5" y="3" width="2" height="2" fill="#fff"/><rect x="5.5" y="3" width="2" height="2" fill="#fff"/>
      <rect x="2.5" y="7" width="2" height="2" fill="#fff"/><rect x="5.5" y="7" width="2" height="2" fill="#fff"/>
      <circle cx="12.5" cy="8" r="2" fill="#1a1a1a"/>
      <path d="M9.5 16 V13 Q9.5 10.8 12.5 10.8 Q15.5 10.8 15.5 13 V16 Z" fill="#1a1a1a"/>
    </svg>
    <div class="col-card col-card--narrow" style="left:236px">
      <h3>3rd Column</h3>
      <p>Lorem Ipsum is simply dummy text of the printing and typesetting industry. Lorem Ipsum has been the industry's standard dummy text ever.</p>
    </div>
    <footer class="slide-foot"><span class="web-address">www.webaddress.com</span><span class="page-number">6</span></footer>
  </section>

</div>
</body>
</html>
```